PSD Designs needed to give to my Developer

Hello, I need PSD files to give to my programmer for the creation of my new website. The website is for ORA quarter, a new clothing company based in Chicago, IL. We sell womens, mens and kids fashion. We specialize in jackets, outerwear and sweaters, but we sell clothing from every category, I have someone working on the logo, so I can't include it for reference. However, I have included 2 reference sites as well as a PDF of how the 2 reference sites could be merged together. The main company color should be blue (hence the name ORA quarter), and the overall feel of the site should be FUN. It should communicate: This is where you want to shop if you want a FUN, HAPPY experience. I need the Home Page file designed very quickly. Whoever is awarded this job will immediately continue working with me to design the other 8 pages. I will pay for all pages. The amount I am offering is for this one page only, and I will pay you additional to design all other 8 pages. Thank you for your time and I will be picking the best design so that we can immediately build a great relationship and work through the rest of the project.

Industry/Entity Type

Apparel Store

Number of Pages Required

1 page

Font styles to use
Sans Serif

Colors
33a6d7
0492cd
ffffff

Requirements
Must have
• I have included all notes in the project description so please check there. My project must communicate: Fun and Happy Design. Even tho I have chosen a few variations of blue below, I still want the designer to incorporate other colors as necessary to acheive the desired look.
Should not have
• It should have a boring, childish feel

```html
<!DOCTYPE html>
<html lang="en">
<head>
<meta charset="utf-8">
<title>ORA quarter — Home</title>
<link href="https://fonts.googleapis.com/css2?family=Arimo:wght@400;700&family=Fira+Sans+Extra+Condensed:wght@300;400;500;600&display=swap" rel="stylesheet">
<style>
  :root{
    --sky:#6dcdf4;
    --bar:#05a6e4;
    --navy:#0d4f9f;
    --login:#0d5aa7;
    --ink:#222;
    --white:#fff;
    --magenta:#e6138b;
    --story-ink:#3b2b3b;
    --movement-ink:rgba(125,88,66,.8);
  }
  *{margin:0;padding:0;box-sizing:border-box}
  html,body{width:718px;height:1200px;overflow:hidden;background:var(--white)}
  body{position:relative;font-family:"Fira Sans Extra Condensed",sans-serif;color:var(--ink)}

  .promo-bar{position:absolute;left:110px;top:0;width:530px;height:18px;background:var(--bar);color:var(--white);font-size:9px;line-height:18px;padding-left:9px}
  .promo-bar strong{font-weight:600}
  .login{position:absolute;right:0;top:0;width:70px;height:18px;background:var(--login);text-align:center;font-size:10px}

  .site-header{position:absolute;left:0;top:18px;width:718px;height:62px;background:var(--white)}
  .brand{position:absolute;left:116px;top:25px;display:flex;align-items:center;gap:6px;font-size:19px;font-weight:500;color:var(--bar)}
  .brand-mark{width:9px;height:9px;background:var(--bar);border-radius:50%}
  .nav{position:absolute;top:33px;left:0;width:718px;font-size:9px;font-weight:400;white-space:nowrap}
  .nav span{position:absolute}

  .hero{position:absolute;left:0;top:80px;width:718px;height:438px;background:var(--sky)}
  .hero svg{position:absolute;left:0;top:0}
  .cta{position:absolute;left:260px;top:166px;width:208px;height:48px;border:3px solid var(--white);color:var(--white);font-family:"Arimo",sans-serif;font-weight:700;font-size:31px;text-align:center;line-height:42px}
  .cta-note{position:absolute;left:200px;top:229px;width:330px;text-align:center;color:var(--white);font-family:"Arimo",sans-serif;font-size:22px;line-height:22.5px}
  .cta-note b{display:block;font-size:23px}

  .story{position:absolute;left:0;top:518px;width:718px;height:374px;background:linear-gradient(100deg,#e9e4dc 0%,#c9b3a4 35%,#b88f7c 55%,#d8c3bd 75%,#9fa3b6 100%)}
  .story-title{position:absolute;left:112px;top:152px;color:var(--story-ink);font-size:50px;line-height:38px;letter-spacing:-1px}
  .story-title .light{display:block;padding-left:22px;font-weight:300}
  .story-title .bold{display:block;font-weight:600}

  .shop-tile{position:absolute;left:0;top:892px;width:384px;height:260px;background:linear-gradient(90deg,#7d5f5a 0%,#e98aa6 25%,#e9584f 45%,#d9c9c0 70%,#ece3dc 100%)}
  .shop-tile h3{position:absolute;left:222px;top:100px;font-size:54px;line-height:54px;font-weight:600;color:var(--magenta)}

  .movement-tile{position:absolute;left:384px;top:892px;width:334px;height:260px;background:linear-gradient(180deg,#fbfbfb 0%,#f0ddd0 40%,#a4744d 70%,#8b5b37 100%)}
  .movement-tile h3{position:absolute;left:37px;top:134px;width:266px;text-align:center;font-size:31px;line-height:29px;font-weight:600;color:var(--movement-ink)}

  .site-footer{position:absolute;left:0;top:1152px;width:718px;height:48px;background:var(--navy);color:var(--white);font-size:9px}
  .copyright{position:absolute;left:101px;top:21px}
  .site-footer .nav{top:21px}
</style>
</head>
<body>
  <div class="promo-bar">Pop-up your own ORA Boulevard for ONLY <strong>$99</strong>
    <div class="login">LOGIN</div>
  </div>

  <header class="site-header">
    <div class="brand"><span class="brand-mark"></span>ORA quarter</div>
    <nav class="nav">
      <span style="left:358px">HOME</span>
      <span style="left:390px">GET TO KNOW US</span>
      <span style="left:462px">WHY ORA?</span>
      <span style="left:509px">HOST A POP-UP</span>
      <span style="left:578px">BECOME A STYLIST</span>
    </nav>
  </header>

  <section class="hero">
    <svg width="718" height="438" viewBox="0 0 718 438">
      <defs>
        <linearGradient id="cloud-tone" x1="0" x2="1"><stop offset=".5" stop-color="#fff"/><stop offset=".5" stop-color="#fbeee0"/></linearGradient>
        <linearGradient id="basket-tone" x1="0" y1="0" x2="0" y2="1"><stop offset=".25" stop-color="#3bb54a"/><stop offset=".25" stop-color="#f4c21b"/><stop offset="1" stop-color="#e8322b"/></linearGradient>
        <linearGradient id="bag-tone" x1="0" y1="0" x2="1" y2="1"><stop offset="0" stop-color="#1c5ea8"/><stop offset="1" stop-color="#123f78"/></linearGradient>
        <linearGradient id="gift-tone" x1="0" y1="0" x2="1" y2="1"><stop offset="0" stop-color="#5fb4ea"/><stop offset=".5" stop-color="#3c8fd8"/><stop offset="1" stop-color="#d8333a"/></linearGradient>
        <linearGradient id="cart-tone" x1="0" y1="0" x2="1" y2="1"><stop offset="0" stop-color="#1e5fae"/><stop offset="1" stop-color="#3a8be0"/></linearGradient>
        <linearGradient id="tag-tone" x1="0" x2="1"><stop offset=".45" stop-color="#fff"/><stop offset=".55" stop-color="#e5282e"/></linearGradient>
        <linearGradient id="wallet-tone" x1="0" y1="0" x2="0" y2="1"><stop offset=".12" stop-color="#2fb24b"/><stop offset=".12" stop-color="#4aa3e6"/><stop offset="1" stop-color="#2c7cc8"/></linearGradient>
      </defs>
      <g stroke="#fff" stroke-width="1">
        <line x1="92" y1="0" x2="92" y2="304"/>
        <line x1="130" y1="0" x2="130" y2="192"/>
        <line x1="174" y1="0" x2="174" y2="86"/>
        <line x1="234" y1="0" x2="234" y2="322"/>
        <line x1="296" y1="0" x2="296" y2="62"/>
        <line x1="422" y1="0" x2="422" y2="68"/>
        <line x1="505" y1="0" x2="505" y2="298"/>
        <line x1="548" y1="0" x2="548" y2="94"/>
        <line x1="606" y1="0" x2="606" y2="230"/>
        <line x1="638" y1="0" x2="638" y2="340"/>
      </g>
      <g role="img" aria-label="Paper cloud">
        <rect x="144" y="86" width="64" height="36" rx="18" fill="url(#cloud-tone)"/></g>
      <g role="img" aria-label="Paper cloud">
        <rect x="394" y="68" width="64" height="36" rx="18" fill="url(#cloud-tone)"/></g>
      <g role="img" aria-label="Paper cloud">
        <rect x="576" y="230" width="66" height="36" rx="18" fill="url(#cloud-tone)"/></g>
      <g role="img" aria-label="Paper cloud">
        <rect x="62" y="304" width="64" height="38" rx="19" fill="url(#cloud-tone)"/></g>
      <g role="img" aria-label="Paper shopping basket in green, yellow and red">
        <rect x="268" y="62" width="64" height="62" rx="6" fill="url(#basket-tone)"/></g>
      <g role="img" aria-label="Navy paper shopping bag">
        <rect x="514" y="94" width="50" height="58" rx="4" fill="url(#bag-tone)"/></g>
      <g role="img" aria-label="Blue gift box with red ribbon">
        <rect x="112" y="192" width="68" height="76" rx="5" fill="url(#gift-tone)"/></g>
      <g role="img" aria-label="Blue shopping cart">
        <rect x="206" y="322" width="68" height="76" rx="6" fill="url(#cart-tone)"/></g>
      <g role="img" aria-label="White and red dollar price tags">
        <rect x="476" y="298" width="66" height="80" rx="6" fill="url(#tag-tone)"/></g>
      <g role="img" aria-label="Blue wallet with green bill">
        <rect x="602" y="340" width="64" height="60" rx="8" fill="url(#wallet-tone)"/></g>
    </svg>
    <div class="cta">SHOP NOW</div>
    <p class="cta-note"><b>LIMITED INVENTORY</b>that’s only available for<br>ONE week!</p>
  </section>

  <section class="story" role="img" aria-label="Smiling family of mother, father and daughter at home">
    <h2 class="story-title"><span class="light">OUR</span><span class="bold">STORY</span></h2>
  </section>

  <section class="shop-tile" role="img" aria-label="Two friends smiling with shopping bags in a mall">
    <h3>SHOP</h3>
  </section>

  <section class="movement-tile" role="img" aria-label="Smiling older man in a brown leather jacket">
    <h3>BE HAPPIER,<br>JOIN THE MOVEMENT</h3>
  </section>

  <footer class="site-footer">
    <span class="copyright">Copyright © 2018 ORA</span>
    <nav class="nav">
      <span style="left:358px">HOME</span>
      <span style="left:390px">GET TO KNOW US</span>
      <span style="left:462px">WHY ORA?</span>
      <span style="left:509px">HOST A POP-UP</span>
      <span style="left:578px">BECOME A STYLIST</span>
    </nav>
  </footer>
</body>
</html>
```